Business card for a young aspring actress

My daughter is 18 and just starting out on her profession as an actress. She is a member of the Open Stage Company and has already had some extras work and a featured role in an upcoming Feature film.

She wants/needs a card that she can have to hand to give to those she comes into contact with in the theatre, TV and film industries.

We are thinking that it may be double sided with an impact side including a picture of her and her name etc with the reverse holding contact and other details.

She wants to go by the name Maren Joy Whitcombe.

She has done a little modelling but sees herself as an actress.

She can be seen in this video
http://www.hollybankacademy.example/videos/a3f19c7d5e2b8406c1d9e7f2a4b60835?width=640&height=480

Target Market(s)

Anyone she comes into contact with in theatre TV and film industries.

Industry/Entity Type

Business

Requirements
Nice to have
• She has email and a website www.marenwhitcombe.example She is quite a connected girl

```html
<!DOCTYPE html>
<html lang="en">
<head>
<meta charset="utf-8">
<title>Maren Joy Whitcombe – Business Card</title>
<link rel="stylesheet" href="https://fonts.googleapis.com/css2?family=Tinos:ital,wght@1,700&display=swap">
<style>
  :root {
    --crimson: #9c0a3e;
    --deep-pink: #a3124f;
    --card-pink: #c91f63;
    --teal: #00827f;
    --teal-shadow: #005e5b;
    --gold: #f4c93e;
    --stone: #c3c7cd;
    --photo-light: #e4e4e4;
    --photo-dark: #7a7a7a;
    --paper: #ffffff;
  }
  * { margin: 0; padding: 0; box-sizing: border-box; }
  html, body { width: 1200px; height: 800px; overflow: hidden; background: var(--paper); }
  body { font-family: "Tinos", "Times New Roman", serif; font-style: italic; font-weight: 700; font-variant: small-caps; }
  .sheet { position: relative; width: 1200px; height: 800px; }

  .card-front { position: absolute; left: 0; top: 0; width: 700px; height: 400px; background: var(--stone); }
  .portrait { position: absolute; left: 0; top: 0; width: 240px; height: 400px;
    background: linear-gradient(160deg, var(--photo-light) 0%, #bdbdbd 55%, var(--photo-dark) 100%); }
  .front-name { position: absolute; left: 240px; width: 460px; top: 33px; text-align: center;
    font-size: 28px; color: var(--crimson); }

  .card-back { position: absolute; left: 0; top: 400px; width: 700px; height: 400px; background: var(--card-pink); overflow: hidden; }
  .stripe { position: absolute; left: 0; top: 0; }
  .website { position: absolute; left: 52px; top: 38px; font-size: 22px; font-variant: normal; color: var(--deep-pink); }
  .name-band { position: absolute; left: 0; top: 68px; width: 700px; height: 72px; background: var(--teal);
    box-shadow: 0 3px 4px rgba(0,0,0,0.35); }
  .band-name { position: absolute; right: 58px; top: 22px; font-size: 28px; color: var(--crimson); }
  .roles { position: absolute; left: 550px; top: 148px; font-size: 22px; line-height: 29px; color: var(--deep-pink); }
  .social { position: absolute; left: 27px; top: 276px; list-style: none; }
  .social li { display: flex; align-items: center; height: 32px; font-size: 18px; color: var(--deep-pink); }
  .social .mark { width: 24px; height: 24px; background: var(--paper); margin-right: 8px; }

  .label { position: absolute; color: var(--crimson); text-align: center; font-size: 22px; line-height: 30px; }
  .label-front { left: 720px; top: 82px; width: 230px; }
  .label-front .big { font-size: 26px; }
  .label-back { left: 752px; top: 532px; font-size: 26px; }
</style>
</head>
<body>
<main class="sheet">
  <section class="card-front">
    <div class="portrait" role="img" aria-label="Black and white portrait photograph of the actress"></div>
    <h1 class="front-name">Maren Joy Whitcombe</h1>
  </section>

  <section class="card-back">
    <svg class="stripe" width="700" height="400" viewBox="0 0 700 400" aria-hidden="true">
      <polygon points="0,170 700,0 700,6 0,178" fill="rgba(0,0,0,0.25)"/>
      <polygon points="0,164 700,-6 700,4 0,174" fill="var(--gold)"/>
    </svg>
    <p class="website">www.marenwhitcombe.example</p>
    <div class="name-band"><h2 class="band-name">Maren Joy Whitcombe</h2></div>
    <p class="roles">Actress<br>Model</p>
    <ul class="social">
      <li><span class="mark"></span>vidstream.example/user/YOURUSERNAME</li>
      <li><span class="mark"></span>www.friendspage.example/pages/yourname/9999999999</li>
      <li><span class="mark"></span>www.chirper.example/USERNAME</li>
    </ul>
  </section>

  <p class="label label-front">Front<br>with space for<br><span class="big">Autograph</span></p>
  <p class="label label-back">Back</p>
</main>
</body>
</html>
```